Norvel Insight - what matters when choosing suppliers

We are a consultancy firm called Norvel Insight specializing in customer strategies. We would like to a more illustrative design of the attached graphic.

The graph shows what is important for B2B companies when choosing suppliers. On the left we have the statistical importance and on the right we have the "asked" importance ("on a scale from 1-10, how important is...." ).

Hope it makes sense! :-)

Target Market(s)

B2B Companies

Industry/Entity Type

Business Consultant

```html
<!DOCTYPE html>
<html lang="en">
<head>
<meta charset="utf-8">
<title>Norvel Insight – Importance of business drivers</title>
<link rel="stylesheet" href="https://fonts.googleapis.com/css2?family=Source+Sans+3:ital,wght@0,400;0,700;1,400&display=swap">
<style>
  :root {
    --ink-heading: #2e5159;
    --ink-label: #2f4a52;
    --ink-note: #2a3f46;
    --track-fill: #f4f4f4;
    --track-edge: #e2e2e2;
    --tick: #6f8087;
    --marker: #e0505a;
    --calc-top: #8d919c;
    --calc-bottom: #4a505d;
    --asked-top: #4fa8d8;
    --asked-bottom: #0b6aa5;
    --page: #ffffff;
  }
  html, body {
    margin: 0;
    padding: 0;
    width: 1200px;
    height: 900px;
    overflow: hidden;
    background: var(--page);
  }
  .figure {
    display: block;
    width: 1200px;
    height: 900px;
    font-family: "Source Sans 3", "Myriad Pro", Arial, sans-serif;
  }
  .figure-title { font-size: 29px; font-weight: 700; fill: var(--ink-heading); }
  .chart-title { font-size: 25px; font-weight: 700; fill: var(--ink-heading); }
  .driver-label { font-size: 25px; fill: var(--ink-label); }
  .footnote { font-size: 20.5px; font-style: italic; fill: var(--ink-note); }
  .track { fill: var(--track-fill); stroke: var(--track-edge); stroke-width: 1; }
  .tick { stroke: var(--tick); stroke-width: 1.2; }
  .average-line { stroke: var(--marker); stroke-width: 1.2; stroke-dasharray: 4 4; }
  .bar-calculated { fill: url(#calcGradient); }
  .bar-asked { fill: url(#askedGradient); }
</style>
</head>
<body>
<svg class="figure" viewBox="0 0 1200 900" xmlns="http://www.w3.org/2000/svg">
  <defs>
    <linearGradient id="calcGradient" x1="0" y1="0" x2="0" y2="1">
      <stop offset="0" stop-color="var(--calc-top)"/>
      <stop offset="1" stop-color="var(--calc-bottom)"/>
    </linearGradient>
    <linearGradient id="askedGradient" x1="0" y1="0" x2="0" y2="1">
      <stop offset="0" stop-color="var(--asked-top)"/>
      <stop offset="1" stop-color="var(--asked-bottom)"/>
    </linearGradient>
  </defs>

  <text class="figure-title" x="65" y="134">Figure 1. Importance of business drivers</text>

  <!-- Calculated importance -->
  <g class="chart chart-calculated">
    <text class="chart-title" x="267" y="208" text-anchor="middle">Calculated importance*</text>
    <g class="axis-ticks">
      <line class="tick" x1="65" y1="241" x2="65" y2="250"/>
      <line class="tick" x1="166" y1="241" x2="166" y2="250"/>
      <line class="tick" x1="268" y1="241" x2="268" y2="250"/>
      <line class="tick" x1="369" y1="241" x2="369" y2="250"/>
      <line class="tick" x1="470" y1="241" x2="470" y2="250"/>
    </g>
    <rect class="track" x="65" y="264" width="405" height="32"/>
    <rect class="bar-calculated" x="101" y="264" width="369" height="32"/>
    <rect class="track" x="65" y="342" width="405" height="32"/>
    <rect class="bar-calculated" x="143" y="342" width="327" height="32"/>
    <rect class="track" x="65" y="420" width="405" height="32"/>
    <rect class="bar-calculated" x="344" y="420" width="126" height="32"/>
    <rect class="track" x="65" y="498" width="405" height="32"/>
    <rect class="bar-calculated" x="363" y="498" width="107" height="32"/>
    <rect class="track" x="65" y="576" width="405" height="32"/>
    <rect class="bar-calculated" x="459" y="576" width="11" height="32"/>
    <line class="average-line" x1="308" y1="252" x2="308" y2="640"/>
  </g>

  <!-- Driver labels -->
  <g class="driver-labels" text-anchor="middle">
    <text class="driver-label" x="597" y="294">Products</text>
    <text class="driver-label" x="597" y="372">Brand</text>
    <text class="driver-label" x="597" y="450">Advice</text>
    <text class="driver-label" x="597" y="528">Delivery</text>
    <text class="driver-label" x="597" y="589">Customer</text>
    <text class="driver-label" x="597" y="614">service</text>
  </g>

  <!-- Asked importance -->
  <g class="chart chart-asked">
    <text class="chart-title" x="932" y="208" text-anchor="middle">Asked importance**</text>
    <g class="axis-ticks">
      <line class="tick" x1="730" y1="241" x2="730" y2="250"/>
      <line class="tick" x1="831" y1="241" x2="831" y2="250"/>
      <line class="tick" x1="932" y1="241" x2="932" y2="250"/>
      <line class="tick" x1="1033" y1="241" x2="1033" y2="250"/>
      <line class="tick" x1="1135" y1="241" x2="1135" y2="250"/>
    </g>
    <rect class="track" x="730" y="264" width="405" height="32"/>
    <rect class="bar-asked" x="730" y="264" width="278" height="32"/>
    <rect class="track" x="730" y="342" width="405" height="32"/>
    <rect class="bar-asked" x="730" y="342" width="22" height="32"/>
    <rect class="track" x="730" y="420" width="405" height="32"/>
    <rect class="bar-asked" x="730" y="420" width="179" height="32"/>
    <rect class="track" x="730" y="498" width="405" height="32"/>
    <rect class="bar-asked" x="730" y="498" width="374" height="32"/>
    <rect class="track" x="730" y="576" width="405" height="32"/>
    <rect class="bar-asked" x="730" y="576" width="196" height="32"/>
    <line class="average-line" x1="891" y1="252" x2="891" y2="640"/>
  </g>

  <!-- Footnotes -->
  <g class="footnotes">
    <text class="footnote" x="65" y="709">*Calculated importance is found through statistical analysis. Partial Least Squares is used to discover</text>
    <text class="footnote" x="65" y="743">the connection between each business driver and loyalty.</text>
    <text class="footnote" x="65" y="777">**Asked importance is found by simply asking customers how important they find each business driver.</text>
  </g>
</svg>
</body>
</html>
```